Pagecraft Design Project

HOME PAGE

BASIC APPROACH
- Clarity and simplicity are most important to me in terms of the home page.

TEXT
- My logo. "Dorvelle Stageworks" (attached) is the name of my company. I've attached the "Dorvelle Stageworks" logo to this note. If the red section doesn't work with our color scheme than it's fine for you to change it to another color

I'd like the logo to be the biggest text on the page. I'd also like it to be situated above all the other text.

- Text line #2 (smaller then Dorvelle Stageworks)
"Producing, Publicizing and Marketing for the Performing Arts"

If you think it would be wise to insert "in the Bay Area" in the first line, please do so.

Text line #3 (and smaller then the text on line #2)
"We bring in the audience, you bring them to their feet."

VISUALS
- Home Page Visual Approach: I'd like a carousel/slider containing 10-12 excellent posters of shows I've produced/publicized to be the visual focus of the page.

Size of the carousel: I'd like it to dominate the page. Make it large and place it in the middle of the page. I would like it to occupy at least 40% of the screen.

I'd like the slides to move continuously on their own. I'd also like them to change relatively slowly so that the images are easy to click on (once clicked, I'd like the images will include additional info about the shows).

Home page visual theory - I think the carousal will make the home page dynamic. The variety of posters offers potential clients the chance to see just how much good work my company has done. I think the images do a better job of relaying a history of our involvement in the local theater scene more eloquently then text. There will be text, just not on the home page.

I also like white space so the home page (or any page looks crowded)

I also don't like long continuos home pages. Just one page that does not exceed the size of the page. In essence, there is nothing below the fold.

Here are examples of webpages I like:

http://www.ninetysixteen.example/ (carousel in place of "our reel")

http://pilotgrove.example/ (I like the simplicity and how the navigation system is integrated into the design)

http://www.sunnyroute.example/ (this is a very good model for the website I'd like)

http://www.quolamart.example/ (I love the navigation system on this site.)

- From what I've read, we've got to give search engines lots of reasons to land on my site. I like the idea of embedding key words on the homepage that are not visible to the naked eye and including these words in the code as well. I do not want to crowd the home page with lots of text. In fact, I'd like the home page to have very little text.

- One other possible visual element for the home page: A link that takes viewers to a page where they can sign up for my newsletter (I'm open to discussing this. I'm not sure what the best practices are in this regard.)

SLIDER/CAROUSEL
http://zipglider.example/jquery-glider-prism-basic-demo.html
using the "fade" or "stack" effect to advance slides

If you know of more interesting or inventive carousels please send me links to where I can see them.

NAVIGATION SYSTEMS

Navigation system - no more then five tabs (I'd like the tabs to change color once the user has clicked on them so it's clear which tabs have been clicked on)

possible tabs: (I'm not absolutely certain what the tabs will say beyond "About" and "contact info")

- About (the history of, client list(
- Our services
- New to producing/publicity (or maybe a more expansive title that would include a list of "20 questions for producers",
- Examples (need a better name then that) would include past copies of the newsletter, press releases and other materials I've created for shows
- Contact info

Maybe a tab would say "communications" which would include: my blog, newsletter samples and possibly additional marketing materials I've made.

Navigation systems I like:
http://www.veltramoor.example/
2 more navigation systems attached.

and again, I'm very drawn to http://www.quolamart.example/

I need to be able to change the text frequently which is why I was interested in working with pagecraft.

If you have any questions, don't hesitate to contact me. If I inadvertently choose a navigation system that is very complex or expensive please let me know. The same thing goes for the carousal.

I also want to say that if you have another visual idea for a site used by a producer and publicists I'm open to the idea. Unless you have a very innovative way of including a theatre curtain or a spotlight on the website I do not want to use that imagery. I would consider something that is truly innovative.
Updates

I have now guaranteed my project. I look forward to your proposals. I am new at this (creating a website)  so bear with me.

Thanks,
Owen

Target Market(s)

performers of all sorts (though mostly solo performers and theater artists)

Industry/Entity Type

Marketing

```html
<!DOCTYPE html>
<html lang="en">
<head>
<meta charset="utf-8">
<title>Dorvelle Stageworks — Producing, Publicizing and Marketing for the Performing Arts</title>
<link href="https://fonts.googleapis.com/css2?family=Open+Sans:ital,wght@0,400;0,600;0,700;1,400&family=Ubuntu:wght@500;700&display=swap" rel="stylesheet">
<style>
:root{
  --red:#f50a0a;
  --ink:#111111;
  --text:#222222;
  --link:#8e0b0b;
  --muted:#555555;
  --line:#d9d9d9;
  --field:#f1f1f1;
  --field-border:#9a9a9a;
  --page-grey:#d3d4d6;
  --white:#ffffff;
}
*{box-sizing:border-box;margin:0;padding:0}
html,body{width:1200px;height:957px;overflow:hidden;background:var(--white)}
body{position:relative;font-family:"Open Sans",Arial,sans-serif;color:var(--text)}
a{text-decoration:none;color:inherit}

.brand{position:absolute;left:148px;top:4px;display:flex;align-items:center;gap:12px}
.brand-mark{width:22px;height:22px;background:var(--red);flex:none}
.brand-name{font-family:"Ubuntu",Arial,sans-serif;font-weight:700;font-size:37px;line-height:34px;color:var(--ink);text-transform:uppercase;letter-spacing:1px;white-space:nowrap}

.main-nav{position:absolute;top:22px;left:649px}
.main-nav a{position:absolute;top:0;height:28px;line-height:28px;font-weight:700;font-size:14.5px;color:var(--ink);white-space:nowrap}
.main-nav a.is-current{background:var(--red);color:var(--white);padding:0 12px;border-radius:3px}

.tagline{position:absolute;top:88px;left:0;width:1200px;text-align:center;font-family:"Ubuntu",Arial,sans-serif;font-weight:700;font-size:30px;color:var(--ink);letter-spacing:-.2px;white-space:nowrap}
.subline-row{position:absolute;top:124px;left:0;width:1200px;display:flex;justify-content:center;align-items:center;gap:10px}
.subline{font-style:italic;font-size:20.5px;line-height:28px;color:var(--ink);letter-spacing:.5px;white-space:nowrap}
.btn{display:inline-block;background:var(--red);color:var(--white);font-weight:700;border-radius:4px;text-transform:uppercase;text-align:center;white-space:nowrap}
.btn-learn{width:103px;height:24px;line-height:24px;font-size:13px}

.hero{position:absolute;left:0;top:174px;width:1200px;height:501px;
  background:linear-gradient(180deg,#6b4a34 0%,#8a6246 30%,#5a2a20 70%,#2c1410 100%)}
.slide{position:absolute;left:147px;top:250px;width:905px;height:359px;background:var(--white);border:1px solid #bdbdbd;box-shadow:0 1px 3px rgba(0,0,0,.3)}
.slide-posters{position:absolute;left:22px;top:17px;width:508px;height:326px;
  background:linear-gradient(100deg,#d9a928 0%,#3a3a3a 45%,#4f8fd4 70%,#a6c6ea 100%)}
.slide-title{position:absolute;left:554px;top:44px;width:345px;font-family:"Ubuntu",Arial,sans-serif;font-weight:700;font-size:24.5px;line-height:33px;color:var(--ink)}
.slide-copy{position:absolute;left:554px;top:120px;width:335px;font-size:16.4px;line-height:25.3px;color:var(--text)}
.btn-contact{position:absolute;left:749px;top:248px;width:111px;height:27px;line-height:27px;font-size:13.5px}
.arrow{position:absolute;top:425px;width:36px;height:36px;border-radius:50%;background:#e6e6e6;box-shadow:0 1px 2px rgba(0,0,0,.4)}
.arrow svg{display:block}
.arrow-prev{left:104px}
.arrow-next{left:1058px}

.lower{position:absolute;left:0;top:675px;width:1200px;height:282px;background:var(--page-grey)}
.panel{position:absolute;left:149px;top:646px;width:902px;height:266px;background:var(--white);box-shadow:0 1px 2px rgba(0,0,0,.25)}
.panel h2{position:absolute;top:17px;font-family:"Ubuntu",Arial,sans-serif;font-weight:700;font-size:23px;color:var(--ink);letter-spacing:.6px;white-space:nowrap}

.blog h2{left:29px}
.blog-list{position:absolute;left:30px;top:50px;width:271px;list-style:none}
.blog-list li{height:28.1px;line-height:26px;border-bottom:1px solid var(--line);font-size:14.5px;letter-spacing:.4px;color:var(--link);white-space:nowrap;overflow:hidden}

.about h2{left:327px}
.about-brand{position:absolute;left:325px;top:52px;display:flex;align-items:center;gap:8px}
.about-brand .brand-mark{width:14px;height:14px}
.about-brand .brand-name{font-size:23px;line-height:26px}
.about-copy{position:absolute;left:325px;top:118px;width:278px;font-size:12.6px;line-height:18px;color:var(--text)}
.about-copy a{color:var(--link)}

.mailing h2{left:610px}
.field{position:absolute;height:43px;background:var(--field);border:1px solid var(--field-border);font-style:italic;font-size:15.5px;color:#8a8a8a;padding:0 7px;line-height:41px;white-space:nowrap}
.field-email{left:612px;top:54px;width:266px}
.field-first{left:612px;top:109px;width:138px}
.field-last{left:763px;top:109px;width:115px}
.btn-signup{position:absolute;left:733px;top:161px;width:145px;height:41px;line-height:41px;font-size:16px;border-radius:7px}

.footer-note{position:absolute;top:925px;right:157px;font-size:13px;color:var(--muted);white-space:nowrap}
.sr-keywords{position:absolute;width:1px;height:1px;overflow:hidden;clip:rect(0 0 0 0)}
</style>
</head>
<body>

<header>
  <a class="brand" href="#">
    <span class="brand-mark"></span>
    <span class="brand-name">Dorvelle<br>Stageworks</span>
  </a>
  <nav class="main-nav">
    <a class="is-current" href="#" style="left:0">HOME</a>
    <a href="#" style="left:91px">ABOUT</a>
    <a href="#" style="left:169px">SERVICES</a>
    <a href="#" style="left:266px">BLOG</a>
    <a href="#" style="left:333px">CONTACT</a>
  </nav>
  <h1 class="tagline">Producing, Publicizing and Marketing for the Performing Arts</h1>
  <div class="subline-row">
    <p class="subline">We bring in the audience, you bring them to their feet.</p>
    <a class="btn btn-learn" href="#">Learn more »</a>
  </div>
</header>

<section class="hero" role="img" aria-label="Blurred photograph of a theatre audience giving a standing ovation"></section>

<section class="slide">
  <div class="slide-posters" role="img" aria-label="Fanned stack of three colourful show posters from past productions"></div>
  <h2 class="slide-title">We’re as Passionate as you About Remarkable Theater</h2>
  <p class="slide-copy">Our track record of successful produc­tions speaks for itself. We love helping teams large and small see a full house on opening night. Contact us to see what we can offer you.</p>
  <a class="btn btn-contact" href="#">Contact us »</a>
</section>
<a class="arrow arrow-prev" href="#" aria-label="Previous slide">
  <svg width="36" height="36" viewBox="0 0 36 36"><path d="M21 10 L13 18 L21 26" fill="none" stroke="#555" stroke-width="3.5" stroke-linecap="round" stroke-linejoin="round"/></svg>
</a>
<a class="arrow arrow-next" href="#" aria-label="Next slide">
  <svg width="36" height="36" viewBox="0 0 36 36"><path d="M15 10 L23 18 L15 26" fill="none" stroke="#555" stroke-width="3.5" stroke-linecap="round" stroke-linejoin="round"/></svg>
</a>

<div class="lower"></div>
<section class="panel">
  <div class="blog">
    <h2>Blog</h2>
    <ul class="blog-list">
      <li><a href="#">Lorem ipsum dolor sit amet</a></li>
      <li><a href="#">Duis laoreet viverra velit, eget</a></li>
      <li><a href="#">Mauris ut nibh augue, at elementum</a></li>
      <li><a href="#">Vestibulum nec lectus vehicula velit</a></li>
      <li><a href="#">Phasellus ac purus arcu, ac posuere</a></li>
      <li><a href="#">Nunc eget augue dolor, vitae vulpu</a></li>
    </ul>
  </div>
  <div class="about">
    <h2>About Us</h2>
    <div class="about-brand">
      <span class="brand-mark"></span>
      <span class="brand-name">Dorvelle<br>Stageworks</span>
    </div>
    <p class="about-copy">Fusce vehicula turpis felis. Nunc ac metus lorem. Nullam sodales eros nec est aliquet eget rhoncus massa porta. Nam eleifend tellus ut dui dignissim non aliquet sem pulvinar. Nam sed nisl ligula, et lobort... <a href="#">[Read more]</a></p>
  </div>
  <form class="mailing">
    <h2>Mailing List</h2>
    <div class="field field-email">Email...</div>
    <div class="field field-first">First Name</div>
    <div class="field field-last">Last Name</div>
    <a class="btn btn-signup" href="#">Sign up »</a>
  </form>
</section>

<footer class="footer-note">Copyright © 2013 · Dorvelle Stageworks · Imagined by Bright Kindle Studio</footer>

<p class="sr-keywords">Bay Area theater producer, theater publicity, performing arts marketing, solo performance promotion</p>
</body>
</html>
```